New web design for software product company

Our company, Tracvenna, does big data analytics for system monitoring and root cause analysis. We help large enterprise IT organisations improve service levels and increase efficiency through searching, analysing and visualising log data.

We need a new design for www.tracvenna-example.com.

The primary goal of the site is to drive visitors to download our product.

We are launching a new 2.0 version of our product in mid-July. In addition to updating our web design, we will need to replace all of the current product images on the current site. We have attached several sample images of the new product to help you with your design.

We would like to reuse the existing textual content, videos and logo on the current site.

Industry/Entity Type

It Company

Requirements
Must have
• We would like flat design, and we would like the new site to be responsive and SEO-friendly.

We need to have our customer logos on the front page.

We would expect to receive handcrafted and maintainable css and html files as well as any new images created by the designer. The maintainability of these files is essential.
Nice to have
• We prefer a bootstrap-based design.
Should not have
• Our target audience is a technical end user who works in a large enterprise IT organisation, typically in a support or operational role, e.g. applications, operations or infrastructure support.

```html
<!DOCTYPE html>
<html lang="en">
<head>
<meta charset="utf-8">
<title>Tracvenna – Root Cause Analysis in Real Time</title>
<link href="https://fonts.googleapis.com/css2?family=Open+Sans:wght@300;400;600;700&display=swap" rel="stylesheet">
<style>
:root{
  --blue:#2f86d3;
  --ink:#333a40;
  --muted:#6b7278;
  --light:#a8adb2;
  --line:#e2e4e6;
  --band:#f4f5f6;
  --footer:#ededed;
  --button-dark:#2f3236;
  --white:#ffffff;
  --shot-dark:#2b2e33;
  --shot-light:#f3f5f7;
}
*{box-sizing:border-box;margin:0;padding:0}
html,body{width:669px;height:1200px;overflow:hidden}
body{font-family:"Open Sans",Arial,sans-serif;color:var(--ink);background:var(--white);position:relative}
.abs{position:absolute}

/* header */
.site-header{position:absolute;top:0;left:0;width:669px;height:33px;background:var(--white)}
.brand{left:89px;top:8px;display:flex;align-items:center;gap:6px;font-weight:700;font-size:14px;color:var(--ink);letter-spacing:.5px}
.brand-dot{width:12px;height:12px;border-radius:50%;background:var(--blue)}
.main-nav a{position:absolute;top:12px;font-size:8px;color:var(--ink);text-decoration:none}
.btn-try{left:519px;top:6px;width:49px;height:20px;background:var(--blue);color:var(--white);font-size:7px;font-weight:700;display:flex;align-items:center;justify-content:center}

/* hero */
.hero{position:absolute;top:33px;left:0;width:669px;height:145px;background:var(--blue)}
.hero-shot{left:87px;top:15px;width:256px;height:114px;background:linear-gradient(90deg,var(--shot-dark) 0 14%,var(--shot-light) 14% 100%);border:3px solid #24272b}
.hero-title{left:369px;top:24px;color:var(--white);font-size:14px;font-weight:600}
.hero-list{left:373px;top:52px;list-style:none;color:#d6e8f7;font-size:8px}
.hero-list li{height:19px;display:flex;align-items:center;gap:9px}
.tick{width:8px;height:8px}

/* download strip */
.download{position:absolute;top:178px;left:0;width:669px;height:60px;border-bottom:1px solid var(--line)}
.download-text{left:60px;top:25px;width:350px;text-align:right;white-space:nowrap;font-size:8.6px;color:var(--ink)}
.btn-download{left:429px;top:20px;width:135px;height:20px;background:var(--button-dark);color:var(--white);font-size:10px;font-weight:700;letter-spacing:.5px;display:flex;align-items:center;justify-content:center;gap:7px}
.btn-download .circle{width:9px;height:9px;border-radius:50%;background:var(--white);display:flex;align-items:center;justify-content:center}

/* features */
.feature-shot{background:linear-gradient(90deg,var(--shot-dark) 0 22%,var(--shot-light) 22% 100%);border:1px solid #c9cdd1}
.feature-title{font-size:14px;font-weight:300;color:var(--ink);white-space:nowrap}
.feature-text{font-size:8px;line-height:13px;color:var(--muted)}

/* testimonial */
.testimonial{position:absolute;top:591px;left:0;width:669px;height:119px;background:var(--band)}
.quote{left:92px;top:20px;width:312px;font-size:11.8px;line-height:16px;color:var(--ink)}
.quote-author{left:92px;top:92px;font-size:7px;color:var(--muted)}
.quote-author b{color:var(--blue);font-weight:700}
.video{left:407px;top:23px;width:157px;height:74px;background:linear-gradient(135deg,#c9c2b5,#8d8477)}
.play{left:24px;top:12px;width:28px;height:28px;border-radius:50%;background:rgba(80,80,80,.75)}

/* customers */
.customers{position:absolute;top:710px;left:0;width:669px;height:76px;border-bottom:1px solid var(--line)}
.customers-title{left:92px;top:22px;font-size:15px;font-weight:300;color:var(--light);line-height:18px}
.customer{top:30px;font-size:11px;font-weight:700;color:#2a3a6a;white-space:nowrap}

/* footer */
.site-footer{position:absolute;top:786px;left:0;width:669px;height:414px;background:var(--footer)}
.footer-col{top:34px;font-size:7px;line-height:14px}
.footer-col h4{font-size:7.5px;font-weight:700;color:var(--ink);margin-bottom:2px}
.footer-col a{display:block;color:var(--light);text-decoration:none}
.footer-col.strong a{color:var(--ink)}
.footer-brand{left:459px;top:39px;display:flex;align-items:center;gap:5px;font-weight:700;font-size:12px;color:var(--ink)}
.social{top:62px;width:8px;height:8px;border-radius:50%;background:var(--blue)}
.copyright{left:481px;top:79px;font-size:6px;color:var(--muted)}
</style>
</head>
<body>

<header class="site-header">
  <div class="abs brand"><span class="brand-dot"></span>TRACVENNA</div>
  <nav class="main-nav">
    <a style="left:320px">Products</a>
    <a style="left:367px">Apps</a>
    <a style="left:401px">Pricing</a>
    <a style="left:443px">Buy</a>
    <a style="left:473px">About</a>
  </nav>
  <div class="abs btn-try">TRY NOW</div>
</header>

<section class="hero">
  <div class="abs hero-shot" role="img" aria-label="Product screenshot: log dashboard with scatter chart and event table"></div>
  <h1 class="abs hero-title">Root Cause Analysis in Real time</h1>
  <ul class="abs hero-list">
    <li><svg class="tick" viewBox="0 0 8 8"><path d="M1 4.2l2 2 4-4.6" stroke="#9fcbef" stroke-width="1.2" fill="none"/></svg>Troubleshoot &amp; Fix issues quickly</li>
    <li><svg class="tick" viewBox="0 0 8 8"><path d="M1 4.2l2 2 4-4.6" stroke="#9fcbef" stroke-width="1.2" fill="none"/></svg>Improve uptime &amp; Serice levels</li>
    <li><svg class="tick" viewBox="0 0 8 8"><path d="M1 4.2l2 2 4-4.6" stroke="#9fcbef" stroke-width="1.2" fill="none"/></svg>Optimize Technology infrastructure</li>
  </ul>
</section>

<section class="download">
  <p class="abs download-text">Big data analytics for real-time system monitoring and root cause analysis</p>
  <div class="abs btn-download">FREE DOWNLOAD
    <span class="circle"><svg width="5" height="5" viewBox="0 0 5 5"><path d="M2.5 0v4M0.8 2.4l1.7 1.8 1.7-1.8" stroke="#2f3236" fill="none"/></svg></span>
  </div>
</section>

<section class="features">
  <div class="abs feature-shot" style="left:92px;top:265px;width:193px;height:86px" role="img" aria-label="Product screenshot: web traffic bar chart and log search results"></div>
  <h2 class="abs feature-title" style="left:308px;top:276px">Interactively Search &amp; Surf your Log Data</h2>
  <p class="abs feature-text" style="left:308px;top:302px;width:230px">Search real-time streaming and historical data. Apply analytics and filters to slice, dice and refine searches using a variety of visual cues and chart types.</p>

  <h2 class="abs feature-title" style="left:92px;top:379px">Perform Root Cause Analysis</h2>
  <p class="abs feature-text" style="left:92px;top:405px;width:260px">Troubleshoot and fix issues quickly. Zoom in and out to search and analyze raw system and log data.&nbsp; Uncover and address issues with bandwidth, performance and security.</p>
  <div class="abs feature-shot" style="left:376px;top:369px;width:191px;height:89px" role="img" aria-label="Product screenshot: traffic source donut chart and log list"></div>

  <div class="abs feature-shot" style="left:92px;top:477px;width:193px;height:86px" role="img" aria-label="Product screenshot: scatter plot timeline and event table"></div>
  <h2 class="abs feature-title" style="left:308px;top:490px;line-height:16px">"Single Pane of Glass" for<br>DevOps &amp; Monitoring</h2>
  <p class="abs feature-text" style="left:308px;top:526px;width:240px">Give everyone a high-level understanding of what's going on in development and production.</p>
</section>

<section class="testimonial">
  <blockquote class="abs quote">Tracvenna's allowed us to work out and rationalize where our bandwidth costs are going...[and] come up with roadmaps in terms of what is going to save us the most money first.</blockquote>
  <p class="abs quote-author"><b>Martin Hale</b>, Enterprise Architect, Stakeline</p>
  <div class="abs video" role="img" aria-label="Video still of a customer interview">
    <div class="abs play"><svg width="28" height="28" viewBox="0 0 28 28"><path d="M11 8l10 6-10 6z" fill="#fff"/></svg></div>
  </div>
</section>

<section class="customers">
  <h3 class="abs customers-title">Our<br>Customers</h3>
  <span class="abs customer" style="left:199px">Stakeline</span>
  <span class="abs customer" style="left:317px;color:#333a40">Verdis</span>
  <span class="abs customer" style="left:413px;color:#333a40">Lindtal Bank</span>
  <span class="abs customer" style="left:527px">Horizon Research</span>
</section>

<footer class="site-footer">
  <div class="abs footer-col" style="left:100px">
    <h4>Product</h4>
    <a>Overview</a><a>Root Cause Analysis</a><a>Monitoring and DevOps</a><a>Release Information</a>
  </div>
  <div class="abs footer-col" style="left:208px">
    <h4>Help</h4>
    <a>Support</a><a>Documentation</a><a>Forum</a><a>Contact Us</a>
  </div>
  <div class="abs footer-col strong" style="left:293px">
    <h4>Try and Buy</h4>
    <a>Pricing</a><a>Download</a><a>Buy</a>
  </div>
  <div class="abs footer-brand"><span class="brand-dot"></span>TRACVENNA</div>
  <span class="abs social" style="left:491px"></span>
  <span class="abs social" style="left:516px"></span>
  <p class="abs copyright">© 2013 Fluent Labs</p>
</footer>

</body>
</html>
```